Accounting services

Looking for a Business card & Logo design

company name - LUMEN ACCOUNTING & TAXATION SOLUTIONS

name - Corwin Pell

position - Accountant / Business Consultant

email - "undecided"

Tel : (868) 512-4873 / (868) 587-2196

**PUT THESE TO THE BACK**
Accounting - VAT * INCOME/CORP TAX * RETURNS

REGISTRATION - VAT * NIS * Company Registration/Business Plan

Industry/Entity Type

Business

```html
<!DOCTYPE html>
<html lang="en">
<head>
<meta charset="utf-8">
<title>Lumen Accounting &amp; Taxation Solutions – Business Card</title>
<link rel="stylesheet" href="https://fonts.googleapis.com/css2?family=Arimo:wght@400;700&family=Open+Sans:wght@400;700&family=Encode+Sans+Condensed:wght@500&display=swap">
<style>
  :root {
    --page-bg: #e6e8eb;
    --card-white: #ffffff;
    --brand-blue: #35a7e0;
    --back-blue: #38a6dc;
    --ink-gray: #5f6062;
    --text-gray: #4a4b4d;
    --white: #ffffff;
  }
  * { box-sizing: border-box; margin: 0; padding: 0; }
  html, body {
    width: 1200px; height: 900px; overflow: hidden;
    background: var(--page-bg);
  }
  .canvas {
    width: 1200px; height: 900px;
    display: flex; flex-direction: column;
    align-items: center; justify-content: center; gap: 44px;
  }
  .card {
    width: 660px; height: 377px;
    position: relative;
    box-shadow: 0 8px 22px rgba(0,0,0,0.18);
  }
  /* Back side */
  .card-back {
    background: var(--back-blue);
    color: var(--white);
    font-family: "Arimo", Arial, sans-serif;
    display: flex; flex-direction: column;
    align-items: center; justify-content: center;
    text-align: center;
  }
  .service-heading {
    font-weight: 700; font-size: 30px; letter-spacing: 0.5px;
  }
  .service-list {
    font-size: 19px; margin-top: 6px; letter-spacing: 0.3px;
  }
  .service-group + .service-group { margin-top: 34px; }

  /* Front side */
  .card-front {
    background: var(--card-white);
    font-family: "Open Sans", Arial, sans-serif;
  }
  .brand {
    position: absolute; top: 40px; right: 42px;
    display: flex; align-items: center; gap: 16px;
  }
  .brand-dot {
    width: 58px; height: 58px; border-radius: 50%;
    background: var(--brand-blue); flex-shrink: 0;
  }
  .brand-name {
    font-family: "Open Sans", Arial, sans-serif;
    font-weight: 700; color: var(--ink-gray);
    font-size: 19px; line-height: 1.2; letter-spacing: 0.6px;
  }
  .brand-name .lead { display: block; font-size: 36px; line-height: 1.05; letter-spacing: 2px; }

  .person {
    position: absolute; left: 56px; top: 176px;
  }
  .person-name {
    font-size: 38px; font-weight: 400; line-height: 1.1;
  }
  .person-name .first { color: var(--brand-blue); }
  .person-name .last { color: var(--ink-gray); }
  .person-title {
    font-family: "Encode Sans Condensed", "Arial Narrow", sans-serif;
    font-weight: 500; font-size: 18px; color: var(--ink-gray);
    margin-top: 2px;
  }
  .contact {
    position: absolute; left: 56px; top: 262px;
    list-style: none;
    font-size: 20px; color: var(--text-gray);
  }
  .contact li {
    display: flex; align-items: center; gap: 14px;
    height: 32px;
  }
  .contact svg { width: 20px; height: 20px; fill: var(--brand-blue); flex-shrink: 0; }
</style>
</head>
<body>
<main class="canvas">

  <section class="card card-back" aria-label="Business card, back">
    <div class="service-group">
      <h2 class="service-heading">ACCOUNTING</h2>
      <p class="service-list">VAT |&nbsp; INCOME/CORP TAX |&nbsp; RETURNS</p>
    </div>
    <div class="service-group">
      <h2 class="service-heading">REGISTRATION</h2>
      <p class="service-list">VAT * NIS * Company Registration/Business Plan</p>
    </div>
  </section>

  <section class="card card-front" aria-label="Business card, front">
    <div class="brand">
      <span class="brand-dot" aria-hidden="true"></span>
      <p class="brand-name"><span class="lead">LUMEN</span>ACCOUNTING &amp;<br>TAXATION SOLUTIONS</p>
    </div>

    <div class="person">
      <h1 class="person-name"><span class="first">Corwin</span><span class="last">Pell</span></h1>
      <p class="person-title">Accountant / Business Consultant</p>
    </div>

    <ul class="contact">
      <li>
        <svg viewBox="0 0 24 24" aria-hidden="true"><path d="M6.6 10.8a15.1 15.1 0 0 0 6.6 6.6l2.2-2.2c.3-.3.7-.4 1-.2 1.1.4 2.3.6 3.6.6.6 0 1 .4 1 1V20c0 .6-.4 1-1 1A17 17 0 0 1 3 4c0-.6.4-1 1-1h3.5c.6 0 1 .4 1 1 0 1.3.2 2.5.6 3.6.1.3 0 .7-.2 1z"/></svg>
        <span>(868) 512-4873</span>
      </li>
      <li>
        <svg viewBox="0 0 24 24" aria-hidden="true"><path d="M7 1h10a2 2 0 0 1 2 2v18a2 2 0 0 1-2 2H7a2 2 0 0 1-2-2V3a2 2 0 0 1 2-2zm0 3v12h10V4zm5 14a1.5 1.5 0 1 0 0 3 1.5 1.5 0 0 0 0-3z"/></svg>
        <span>(868) 587-2196</span>
      </li>
      <li>
        <svg viewBox="0 0 24 24" aria-hidden="true"><path d="M2 5h20v14H2zm2 2v.5l8 5.5 8-5.5V7zm0 2.9V17h16V9.9l-8 5.5z"/></svg>
        <span>corwinpell@lumenmail.com</span>
      </li>
    </ul>
  </section>

</main>
</body>
</html>
```